Order Management User Interface

I need a new design for our order management screens. They need to be end user friendly and contain the data in an easy to read format. These are online orders. I have attached 3 images from the development solution. For now I just need a new UI and ideally would like it delivered in html so we can easily adapt. The screen has multiple tabs to display the different types of data we store. Ideally the end user needs to see customer focused information first.
I have uploaded an example of a different order view that i like.
Fashion Retail
Coded - Design and coding required
1 page

```html
<!DOCTYPE html>
<html lang="en">
<head>
<meta charset="utf-8">
<title>Order Management</title>
<link href="https://fonts.googleapis.com/css2?family=Poppins:wght@400;500;600;700&display=swap" rel="stylesheet">
<style>
:root{
  --bg:#1f2230;
  --side:#1c1f2b;
  --page:#f5f5f5;
  --card:#ffffff;
  --field:#f4f4f4;
  --ink:#1d1f2b;
  --muted:#8a8c93;
  --line:#e6e6e6;
  --green:#2bd17e;
  --red:#f05252;
  --link:#1d1f2b;
}
*{box-sizing:border-box;margin:0;padding:0}
html,body{width:1200px;height:2912px;overflow:hidden;background:var(--bg);font-family:'Poppins',sans-serif;color:var(--ink)}
.screen{position:absolute;left:130px;width:940px;height:800px;display:flex;overflow:hidden}
.sidebar{width:45px;background:var(--side);display:flex;flex-direction:column;align-items:center;padding-top:24px}
.sidebar .burger{margin-bottom:28px}
.sidebar .nav{display:flex;flex-direction:column;gap:22px;width:100%;align-items:center}
.sidebar .nav svg{display:block}
.sidebar .nav .active{position:relative;width:100%;display:flex;justify-content:center}
.sidebar .nav .active::before{content:"";position:absolute;left:0;top:-5px;width:3px;height:28px;background:var(--green)}
.main{flex:1;background:var(--page);position:relative}
.title{position:absolute;left:26px;top:22px;font-size:20px;font-weight:700}
.topbar{position:absolute;right:28px;top:20px;display:flex;align-items:center;gap:10px}
.avatar{width:34px;height:34px;border-radius:50%;background:linear-gradient(135deg,#f08a4b,#c9532a)}
.user b{display:block;font-size:10.5px;font-weight:700}
.user span{display:block;font-size:8px;color:var(--muted);margin-top:-3px}
.lefttabs{position:absolute;left:28px;top:74px;display:flex;gap:6px}
.tab{height:26px;padding:0 12px;font-size:8.5px;font-weight:700;display:flex;align-items:center;gap:5px;border-radius:6px 6px 0 0;background:var(--card)}
.tab.green{background:var(--green);color:#fff}
.leftcard{position:absolute;left:28px;top:100px;width:224px;height:720px;background:var(--card);border-radius:0 8px 8px 8px;padding:14px 20px 0 20px}
.field label{display:block;font-size:8.5px;font-weight:600;margin-bottom:3px}
.input{height:26px;background:var(--field);border-radius:3px;font-size:10px;color:var(--muted);padding-left:12px;display:flex;align-items:center;justify-content:space-between;padding-right:8px}
.field{margin-bottom:9.5px}
.authority{font-size:8.5px;font-weight:600;display:flex;align-items:center;gap:6px;margin-top:16px}
.check{width:10px;height:10px;background:var(--red);border-radius:2px;display:inline-flex;align-items:center;justify-content:center}
.buttons{display:flex;gap:7px;margin-top:12px}
.btn{height:26px;width:89px;font-size:9.5px;font-weight:700;display:flex;align-items:center;justify-content:center;gap:5px;border-radius:3px}
.btn.save{background:var(--green);color:#fff}
.btn.refresh{background:#e9e9e9}
.righttabs{position:absolute;left:265px;top:74px;width:600px;height:26px;display:flex;align-items:center;font-size:8.5px;font-weight:700;padding-left:8px;gap:20px}
.righttabs .on{background:var(--ink);color:#fff;height:26px;padding:0 14px;display:flex;align-items:center;border-radius:6px 6px 0 0}
.rightcard{position:absolute;left:265px;top:100px;width:600px;height:720px;background:var(--card);border-radius:8px;padding:0 10px}
table{border-collapse:collapse;width:100%}
th{font-size:8px;font-weight:600;text-align:left;height:44px;border-bottom:1px solid var(--line);white-space:nowrap}
.items td{font-size:8.5px;color:#555;vertical-align:middle;height:98.5px;border-bottom:1px solid var(--line)}
.items td.div{border-left:1px solid var(--line)}
.items .sku{font-weight:700;color:var(--link);text-decoration:underline;font-size:10px}
.items .plus{font-weight:700;color:var(--ink);font-size:12px}
.items .prod{line-height:12.5px}
.addr td{font-size:9px;color:#555;height:48.7px;border-bottom:1px solid var(--line)}
.addr td.div{border-left:1px solid var(--line)}
.overlay{position:absolute;left:0;top:0;width:100%;height:100%;background:rgba(20,22,30,.45)}
.modal{position:absolute;left:378px;top:2082px;width:446px;height:469px;background:var(--card);border-radius:4px;padding:32px 38px 0 38px}
.modal h2{font-size:27px;font-weight:700;margin-bottom:26px}
.modal .close{position:absolute;right:31px;top:30px;width:38px;height:38px;border-radius:50%;background:#ececec;display:flex;align-items:center;justify-content:center}
.modal .grid{display:grid;grid-template-columns:1fr 1fr;column-gap:12px;row-gap:9px}
.modal .field{margin:0}
.modal .actions{display:flex;justify-content:center;gap:8px;margin-top:20px}
.modal .btn{width:93px}
.btn.dark{background:var(--ink);color:#fff}
</style>
</head>
<body>

<!-- Screen 1: items -->
<section class="screen" style="top:198px">
  <aside class="sidebar">
    <svg class="burger" width="20" height="15" viewBox="0 0 20 15"><path d="M0 1h20M0 7.5h20M0 14h20" stroke="#fff" stroke-width="2"/></svg>
    <div class="nav">
      <div class="active"><svg width="16" height="14" viewBox="0 0 16 14" fill="none" stroke="#2bd17e" stroke-width="1.4"><path d="M1 1h2.5l2 8h8l1.5-6H4.5"/><circle cx="6.5" cy="12" r="1"/><circle cx="12.5" cy="12" r="1"/></svg></div>
      <svg width="14" height="16" viewBox="0 0 14 16" fill="none" stroke="#fff" stroke-width="1.3"><rect x="2" y="1" width="11" height="14" rx="1"/><path d="M5 5h5M5 8h5M5 11h3"/></svg>
      <svg width="15" height="15" viewBox="0 0 15 15" fill="none" stroke="#fff" stroke-width="1.3"><circle cx="7.5" cy="7.5" r="6"/></svg>
      <svg width="15" height="17" viewBox="0 0 15 17" fill="none" stroke="#fff" stroke-width="1.3"><circle cx="7.5" cy="6" r="4"/><path d="M1 16c1-4 12-4 13 0"/></svg>
      <svg width="17" height="16" viewBox="0 0 17 16" fill="none" stroke="#fff" stroke-width="1.3"><circle cx="6" cy="5" r="3.5"/><path d="M1 15c0-4 9-4 9 0M12 9h4M12 12h4M12 15h4"/></svg>
      <svg width="17" height="12" viewBox="0 0 17 12" fill="none" stroke="#fff" stroke-width="1.3"><path d="M1 6c4-7 11-7 15 0-4 7-11 7-15 0z"/><circle cx="8.5" cy="6" r="2.3"/></svg>
      <svg width="13" height="16" viewBox="0 0 13 16" fill="none" stroke="#fff" stroke-width="1.3"><rect x="1" y="7" width="11" height="8" rx="1"/><path d="M3.5 7V4.5a3 3 0 016 0V7"/></svg>
    </div>
  </aside>
  <div class="main">
    <h1 class="title">Development</h1>
    <div class="topbar">
      <svg width="18" height="18" viewBox="0 0 18 18" fill="none"><rect x="2" y="4" width="11" height="12" rx="1" stroke="#1d1f2b" stroke-width="1.6"/><circle cx="14" cy="4" r="3" fill="#f05252"/></svg>
      <svg width="17" height="17" viewBox="0 0 17 17" fill="none" stroke="#1d1f2b" stroke-width="1.3"><circle cx="8.5" cy="8.5" r="7.5"/><path d="M6.5 6.5a2 2 0 114 0c0 1.5-2 1.5-2 3"/><circle cx="8.5" cy="12.2" r=".5"/></svg>
      <div class="avatar" role="img" aria-label="User profile photo"></div>
      <div class="user"><b>JOHN DOE</b><span>User role</span></div>
      <svg width="8" height="5" viewBox="0 0 8 5"><path d="M1 1l3 3 3-3" stroke="#1d1f2b" fill="none"/></svg>
    </div>
    <div class="lefttabs"><div class="tab green">ORDER SEARCH ⊗</div><div class="tab">ORDER 9670363 ⊗</div></div>
    <div class="leftcard">
      <div class="field"><label>ORDER NO*</label><div class="input">9670363</div></div>
      <div class="field"><label>BRAND*</label><div class="input">Verano</div></div>
      <div class="field"><label>ORDER TYPE*</label><div class="input">Sale</div></div>
      <div class="field"><label>STATUS*</label><div class="input">New</div></div>
      <div class="field"><label>ORIG ORDER NO*</label><div class="input">9670363</div></div>
      <div class="field"><label>REFERENCE*</label><div class="input">9670363</div></div>
      <div class="field"><label>ORDER CHANNEL*</label><div class="input">Standard</div></div>
      <div class="field"><label>LOCATION CODE*</label><div class="input">1301</div></div>
      <div class="field"><label>CUSTOMER NO*</label><div class="input">+08 123 456<span>⇕</span></div></div>
      <div class="field"><label>FIRST NAME*</label><div class="input">John</div></div>
      <div class="field"><label>SURNAME*</label><div class="input">John doe</div></div>
      <div class="field"><label>EMAIL*</label><div class="input">Info@example.com</div></div>
      <div class="authority">AUTHORITY TO LEAVE <span class="check"><svg width="7" height="6" viewBox="0 0 7 6"><path d="M1 3l2 2 3-4" stroke="#fff" fill="none"/></svg></span></div>
      <div class="buttons"><div class="btn save">▣ SAVE</div><div class="btn refresh">↻ REFRESH</div></div>
    </div>
    <nav class="righttabs"><span class="on">ITEMS</span><span>CUSTOMER (S)</span><span>ADDRESSES</span><span>PAYMENTS</span><span>VOUCHERS</span><span>EVENT QUEUES</span><span>UPDATES</span><span>FULFILMENTS</span><span>HISTORY</span></nav>
    <div class="rightcard">
      <table class="items">
        <tr><th style="width:22px"></th><th style="width:66px">SKU</th><th style="width:82px">PRODUCTS</th><th style="width:68px"></th><th style="width:80px">IS DROPSHIP</th><th style="width:62px">QUANTITY</th><th style="width:58px">UNIT RETAIL</th><th style="width:58px">UNIT TAX</th><th style="width:58px">DISCOUNT</th><th>FINAL</th></tr>
        <tr><td class="plus">+</td><td><span class="sku">2230566</span></td><td class="div prod">Vendor<br>Brand<br>Product Code<br>Description<br>Colour (C0de)<br>Size</td><td class="div prod">2002589<br>PJ SET<br>900<br>12/14</td><td class="div">False</td><td class="div">01</td><td class="div">35.00</td><td class="div">3.18</td><td class="div">0.00</td><td class="div">35.00</td></tr>
        <tr><td class="plus">+</td><td><span class="sku">2230566</span></td><td class="div prod">Vendor<br>Brand<br>Product Code<br>Description<br>Colour (C0de)<br>Size</td><td class="div prod">2002589<br>PJ SET<br>900<br>12/14</td><td class="div">False</td><td class="div">01</td><td class="div">35.00</td><td class="div">3.18</td><td class="div">0.00</td><td class="div">35.00</td></tr>
        <tr><td class="plus">+</td><td><span class="sku">2230566</span></td><td class="div prod">Vendor<br>Brand<br>Product Code<br>Description<br>Colour (C0de)<br>Size</td><td class="div prod">2002589<br>PJ SET<br>900<br>12/14</td><td class="div">False</td><td class="div">01</td><td class="div">35.00</td><td class="div">3.18</td><td class="div">0.00</td><td class="div">35.00</td></tr>
        <tr><td class="plus">+</td><td><span class="sku">2230566</span></td><td class="div prod">Vendor<br>Brand<br>Product Code<br>Description<br>Colour (C0de)<br>Size</td><td class="div prod">2002589<br>PJ SET<br>900<br>12/14</td><td class="div">False</td><td class="div">01</td><td class="div">35.00</td><td class="div">3.18</td><td class="div">0.00</td><td class="div">35.00</td></tr>
        <tr><td class="plus">+</td><td><span class="sku">2230566</span></td><td class="div prod">Vendor<br>Brand<br>Product Code<br>Description<br>Colour (C0de)<br>Size</td><td class="div prod">2002589<br>PJ SET<br>900<br>12/14</td><td class="div">False</td><td class="div">01</td><td class="div">35.00</td><td class="div">3.18</td><td class="div">0.00</td><td class="div">35.00</td></tr>
        <tr><td class="plus">+</td><td><span class="sku">2230566</span></td><td class="div prod">Vendor<br>Brand<br>Product Code<br>Description<br>Colour (C0de)<br>Size</td><td class="div prod">2002589<br>PJ SET<br>900<br>12/14</td><td class="div">False</td><td class="div">01</td><td class="div">35.00</td><td class="div">3.18</td><td class="div">0.00</td><td class="div">35.00</td></tr>
        <tr><td class="plus">+</td><td><span class="sku" style="color:#2f5bd3">2230566</span></td><td class="div prod">Vendor<br>Brand<br>Product Code<br>Description<br>Colour (C0de)<br>Size</td><td class="div prod">2002589<br>PJ SET<br>900<br>12/14</td><td class="div">False</td><td class="div">01</td><td class="div">35.00</td><td class="div">3.18</td><td class="div">0.00</td><td class="div">35.00</td></tr>
      </table>
    </div>
  </div>
</section>

<!-- Screen 2: addresses -->
<section class="screen" style="top:1060px;left:132px">
  <aside class="sidebar">
    <svg class="burger" width="20" height="15" viewBox="0 0 20 15"><path d="M0 1h20M0 7.5h20M0 14h20" stroke="#fff" stroke-width="2"/></svg>
    <div class="nav">
      <div class="active"><svg width="16" height="14" viewBox="0 0 16 14" fill="none" stroke="#2bd17e" stroke-width="1.4"><path d="M1 1h2.5l2 8h8l1.5-6H4.5"/><circle cx="6.5" cy="12" r="1"/><circle cx="12.5" cy="12" r="1"/></svg></div>
      <svg width="14" height="16" viewBox="0 0 14 16" fill="none" stroke="#fff" stroke-width="1.3"><rect x="2" y="1" width="11" height="14" rx="1"/><path d="M5 5h5M5 8h5M5 11h3"/></svg>
      <svg width="15" height="15" viewBox="0 0 15 15" fill="none" stroke="#fff" stroke-width="1.3"><circle cx="7.5" cy="7.5" r="6"/></svg>
      <svg width="15" height="17" viewBox="0 0 15 17" fill="none" stroke="#fff" stroke-width="1.3"><circle cx="7.5" cy="6" r="4"/><path d="M1 16c1-4 12-4 13 0"/></svg>
      <svg width="17" height="16" viewBox="0 0 17 16" fill="none" stroke="#fff" stroke-width="1.3"><circle cx="6" cy="5" r="3.5"/><path d="M1 15c0-4 9-4 9 0M12 9h4M12 12h4M12 15h4"/></svg>
      <svg width="17" height="12" viewBox="0 0 17 12" fill="none" stroke="#fff" stroke-width="1.3"><path d="M1 6c4-7 11-7 15 0-4 7-11 7-15 0z"/><circle cx="8.5" cy="6" r="2.3"/></svg>
      <svg width="13" height="16" viewBox="0 0 13 16" fill="none" stroke="#fff" stroke-width="1.3"><rect x="1" y="7" width="11" height="8" rx="1"/><path d="M3.5 7V4.5a3 3 0 016 0V7"/></svg>
    </div>
  </aside>
  <div class="main">
    <h1 class="title">Development</h1>
    <div class="topbar">
      <svg width="18" height="18" viewBox="0 0 18 18" fill="none"><rect x="2" y="4" width="11" height="12" rx="1" stroke="#1d1f2b" stroke-width="1.6"/><circle cx="14" cy="4" r="3" fill="#f05252"/></svg>
      <svg width="17" height="17" viewBox="0 0 17 17" fill="none" stroke="#1d1f2b" stroke-width="1.3"><circle cx="8.5" cy="8.5" r="7.5"/><path d="M6.5 6.5a2 2 0 114 0c0 1.5-2 1.5-2 3"/><circle cx="8.5" cy="12.2" r=".5"/></svg>
      <div class="avatar" role="img" aria-label="User profile photo"></div>
      <div class="user"><b>JOHN DOE</b><span>User role</span></div>
      <svg width="8" height="5" viewBox="0 0 8 5"><path d="M1 1l3 3 3-3" stroke="#1d1f2b" fill="none"/></svg>
    </div>
    <div class="lefttabs"><div class="tab green">ORDER SEARCH ⊗</div><div class="tab">ORDER 9670363 ⊗</div></div>
    <div class="leftcard">
      <div class="field"><label>ORDER NO*</label><div class="input">9670363</div></div>
      <div class="field"><label>BRAND*</label><div class="input">Verano</div></div>
      <div class="field"><label>ORDER TYPE*</label><div class="input">Sale</div></div>
      <div class="field"><label>STATUS*</label><div class="input">New</div></div>
      <div class="field"><label>ORIG ORDER NO*</label><div class="input">9670363</div></div>
      <div class="field"><label>REFERENCE*</label><div class="input">9670363</div></div>
      <div class="field"><label>ORDER CHANNEL*</label><div class="input">Standard</div></div>
      <div class="field"><label>LOCATION CODE*</label><div class="input">1301</div></div>
      <div class="field"><label>CUSTOMER NO*</label><div class="input">+08 123 456<span>⇕</span></div></div>
      <div class="field"><label>FIRST NAME*</label><div class="input">John</div></div>
      <div class="field"><label>SURNAME*</label><div class="input">John doe</div></div>
      <div class="field"><label>EMAIL*</label><div class="input">Info@example.com</div></div>
      <div class="authority">AUTHORITY TO LEAVE <span class="check"><svg width="7" height="6" viewBox="0 0 7 6"><path d="M1 3l2 2 3-4" stroke="#fff" fill="none"/></svg></span></div>
      <div class="buttons"><div class="btn save">▣ SAVE</div><div class="btn refresh">↻ REFRESH</div></div>
    </div>
    <nav class="righttabs"><span>ITEMS</span><span>CUSTOMER (S)</span><span class="on">ADDRESSES</span><span>PAYMENTS</span><span>VOUCHERS</span><span>EVENT QUEUES</span><span>UPDATES</span><span>FULFILMENTS</span><span>HISTORY</span></nav>
    <div class="rightcard">
      <table class="addr">
        <tr><th style="width:84px;padding-left:28px">TYPE</th><th style="width:85px">NAME</th><th style="width:150px">ATTENTION OF</th><th style="width:146px">ADDRESS</th><th>EMAIL</th></tr>
        <tr><td style="padding-left:28px">Delivery</td><td>Test Order</td><td class="div"></td><td class="div">Some address line here</td><td>info@example.com</td></tr>
        <tr><td style="padding-left:28px">Delivery</td><td>Test Order</td><td class="div"></td><td class="div">Some address line here</td><td>info@example.com</td></tr>
        <tr><td style="padding-left:28px">Delivery</td><td>Test Order</td><td class="div"></td><td class="div">Some address line here</td><td>info@example.com</td></tr>
        <tr><td style="padding-left:28px">Delivery</td><td>Test Order</td><td class="div"></td><td class="div">Some address line here</td><td>info@example.com</td></tr>
        <tr><td style="padding-left:28px">Delivery</td><td>Test Order</td><td class="div"></td><td class="div">Some address line here</td><td>info@example.com</td></tr>
        <tr><td style="padding-left:28px">Delivery</td><td>Test Order</td><td class="div"></td><td class="div">Some address line here</td><td>info@example.com</td></tr>
        <tr><td style="padding-left:28px">Delivery</td><td>Test Order</td><td class="div"></td><td class="div">Some address line here</td><td>info@example.com</td></tr>
        <tr><td style="padding-left:28px">Delivery</td><td>Test Order</td><td class="div"></td><td class="div">Some address line here</td><td>info@example.com</td></tr>
        <tr><td style="padding-left:28px">Delivery</td><td>Test Order</td><td class="div"></td><td class="div">Some address line here</td><td>info@example.com</td></tr>
        <tr><td style="padding-left:28px">Delivery</td><td>Test Order</td><td class="div"></td><td class="div">Some address line here</td><td>info@example.com</td></tr>
        <tr><td style="padding-left:28px">Delivery</td><td>Test Order</td><td class="div"></td><td class="div">Some address line here</td><td>info@example.com</td></tr>
        <tr><td style="padding-left:28px">Delivery</td><td>Test Order</td><td class="div"></td><td class="div">Some address line here</td><td>info@example.com</td></tr>
        <tr><td style="padding-left:28px">Delivery</td><td>Test Order</td><td class="div"></td><td class="div">Some address line here</td><td>info@example.com</td></tr>
      </table>
    </div>
  </div>
</section>

<!-- Screen 3: address edit dialog -->
<section class="screen" style="top:1917px;left:132px">
  <aside class="sidebar">
    <svg class="burger" width="20" height="15" viewBox="0 0 20 15"><path d="M0 1h20M0 7.5h20M0 14h20" stroke="#fff" stroke-width="2"/></svg>
    <div class="nav">
      <div class="active"><svg width="16" height="14" viewBox="0 0 16 14" fill="none" stroke="#2bd17e" stroke-width="1.4"><path d="M1 1h2.5l2 8h8l1.5-6H4.5"/><circle cx="6.5" cy="12" r="1"/><circle cx="12.5" cy="12" r="1"/></svg></div>
      <svg width="14" height="16" viewBox="0 0 14 16" fill="none" stroke="#fff" stroke-width="1.3"><rect x="2" y="1" width="11" height="14" rx="1"/><path d="M5 5h5M5 8h5M5 11h3"/></svg>
      <svg width="15" height="15" viewBox="0 0 15 15" fill="none" stroke="#fff" stroke-width="1.3"><circle cx="7.5" cy="7.5" r="6"/></svg>
      <svg width="15" height="17" viewBox="0 0 15 17" fill="none" stroke="#fff" stroke-width="1.3"><circle cx="7.5" cy="6" r="4"/><path d="M1 16c1-4 12-4 13 0"/></svg>
      <svg width="17" height="16" viewBox="0 0 17 16" fill="none" stroke="#fff" stroke-width="1.3"><circle cx="6" cy="5" r="3.5"/><path d="M1 15c0-4 9-4 9 0M12 9h4M12 12h4M12 15h4"/></svg>
      <svg width="17" height="12" viewBox="0 0 17 12" fill="none" stroke="#fff" stroke-width="1.3"><path d="M1 6c4-7 11-7 15 0-4 7-11 7-15 0z"/><circle cx="8.5" cy="6" r="2.3"/></svg>
      <svg width="13" height="16" viewBox="0 0 13 16" fill="none" stroke="#fff" stroke-width="1.3"><rect x="1" y="7" width="11" height="8" rx="1"/><path d="M3.5 7V4.5a3 3 0 016 0V7"/></svg>
    </div>
  </aside>
  <div class="main">
    <h1 class="title">Development</h1>
    <div class="topbar">
      <svg width="18" height="18" viewBox="0 0 18 18" fill="none"><rect x="2" y="4" width="11" height="12" rx="1" stroke="#1d1f2b" stroke-width="1.6"/><circle cx="14" cy="4" r="3" fill="#f05252"/></svg>
      <svg width="17" height="17" viewBox="0 0 17 17" fill="none" stroke="#1d1f2b" stroke-width="1.3"><circle cx="8.5" cy="8.5" r="7.5"/><path d="M6.5 6.5a2 2 0 114 0c0 1.5-2 1.5-2 3"/><circle cx="8.5" cy="12.2" r=".5"/></svg>
      <div class="avatar" role="img" aria-label="User profile photo"></div>
      <div class="user"><b>JOHN DOE</b><span>User role</span></div>
      <svg width="8" height="5" viewBox="0 0 8 5"><path d="M1 1l3 3 3-3" stroke="#1d1f2b" fill="none"/></svg>
    </div>
    <div class="lefttabs"><div class="tab green">ORDER SEARCH ⊗</div><div class="tab">ORDER 9670363 ⊗</div></div>
    <div class="leftcard">
      <div class="field"><label>ORDER NO*</label><div class="input">9670363</div></div>
      <div class="field"><label>BRAND*</label><div class="input">Verano</div></div>
      <div class="field"><label>ORDER TYPE*</label><div class="input">Sale</div></div>
      <div class="field"><label>STATUS*</label><div class="input">New</div></div>
      <div class="field"><label>ORIG ORDER NO*</label><div class="input">9670363</div></div>
      <div class="field"><label>REFERENCE*</label><div class="input">9670363</div></div>
      <div class="field"><label>ORDER CHANNEL*</label><div class="input">Standard</div></div>
      <div class="field"><label>LOCATION CODE*</label><div class="input">1301</div></div>
      <div class="field"><label>CUSTOMER NO*</label><div class="input">+08 123 456</div></div>
      <div class="field"><label>FIRST NAME*</label><div class="input">John</div></div>
      <div class="field"><label>SURNAME*</label><div class="input">John doe</div></div>
      <div class="field"><label>EMAIL*</label><div class="input">Info@example.com</div></div>
      <div class="authority">AUTHORITY TO LEAVE <span class="check"><svg width="7" height="6" viewBox="0 0 7 6"><path d="M1 3l2 2 3-4" stroke="#fff" fill="none"/></svg></span></div>
      <div class="buttons"><div class="btn save">▣ SAVE</div><div class="btn refresh">↻ REFRESH</div></div>
    </div>
    <nav class="righttabs"><span>ITEMS</span><span>CUSTOMER (S)</span><span class="on">ADDRESSES</span><span>PAYMENTS</span><span>VOUCHERS</span><span>EVENT QUEUES</span><span>UPDATES</span><span>FULFILMENTS</span><span>HISTORY</span></nav>
    <div class="rightcard">
      <table class="addr">
        <tr><th style="width:84px;padding-left:28px">TYPE</th><th style="width:85px">NAME</th><th style="width:150px">ATTENTION OF</th><th style="width:146px">ADDRESS</th><th>EMAIL</th></tr>
        <tr><td style="padding-left:28px">Delivery</td><td>Test Order</td><td class="div"></td><td class="div">Some address line here</td><td>info@example.com</td></tr>
        <tr><td style="padding-left:28px">Delivery</td><td>Test Order</td><td class="div"></td><td class="div">Some address line here</td><td>info@example.com</td></tr>
        <tr><td style="padding-left:28px">Delivery</td><td>Test Order</td><td class="div"></td><td class="div">Some address line here</td><td>info@example.com</td></tr>
        <tr><td style="padding-left:28px">Delivery</td><td>Test Order</td><td class="div"></td><td class="div">Some address line here</td><td>info@example.com</td></tr>
        <tr><td style="padding-left:28px">Delivery</td><td>Test Order</td><td class="div"></td><td class="div">Some address line here</td><td>info@example.com</td></tr>
        <tr><td style="padding-left:28px">Delivery</td><td>Test Order</td><td class="div"></td><td class="div">Some address line here</td><td>info@example.com</td></tr>
        <tr><td style="padding-left:28px">Delivery</td><td>Test Order</td><td class="div"></td><td class="div">Some address line here</td><td>info@example.com</td></tr>
        <tr><td style="padding-left:28px">Delivery</td><td>Test Order</td><td class="div"></td><td class="div">Some address line here</td><td>info@example.com</td></tr>
        <tr><td style="padding-left:28px">Delivery</td><td>Test Order</td><td class="div"></td><td class="div">Some address line here</td><td>info@example.com</td></tr>
        <tr><td style="padding-left:28px">Delivery</td><td>Test Order</td><td class="div"></td><td class="div">Some address line here</td><td>info@example.com</td></tr>
        <tr><td style="padding-left:28px">Delivery</td><td>Test Order</td><td class="div"></td><td class="div">Some address line here</td><td>info@example.com</td></tr>
        <tr><td style="padding-left:28px">Delivery</td><td>Test Order</td><td class="div"></td><td class="div">Some address line here</td><td>info@example.com</td></tr>
        <tr><td style="padding-left:28px">Delivery</td><td>Test Order</td><td class="div"></td><td class="div">Some address line here</td><td>info@example.com</td></tr>
      </table>
    </div>
  </div>
  <div class="overlay"></div>
</section>

<div class="modal">
  <h2>Address</h2>
  <div class="close"><svg width="12" height="12" viewBox="0 0 12 12"><path d="M1 1l10 10M11 1L1 11" stroke="#1d1f2b" stroke-width="1.5"/></svg></div>
  <div class="grid">
    <div class="field"><label>FIRST NAME*</label><div class="input">John</div></div>
    <div class="field"><label>SURNAME*</label><div class="input">John doe</div></div>
    <div class="field"><label>ATTENTION OF*</label><div class="input">Sale</div></div>
    <div class="field"><label>ADDRESS 1*</label><div class="input">Some address here</div></div>
    <div class="field"><label>ADDRESS 2*</label><div class="input">Some address here</div></div>
    <div class="field"><label>SUBERB*</label><div class="input">9670363</div></div>
    <div class="field"><label>CITY*</label><div class="input">USA</div></div>
    <div class="field"><label>STATE*</label><div class="input">Type here</div></div>
    <div class="field"><label>POSTCODE*</label><div class="input">9670363</div></div>
    <div class="field"><label>COUNTRY*</label><div class="input">Malysia</div></div>
    <div class="field"><label>EMAIL*</label><div class="input">Info@example.com</div></div>
    <div class="field"><label>PHONE*</label><div class="input">+08 123 456 789</div></div>
  </div>
  <div class="actions"><div class="btn save">UPDATE</div><div class="btn dark">CANCEL</div></div>
</div>

</body>
</html>
```